Website Design for A Leading Live Casino Software Provider

We provide live casino software to other land based and online gaming establishments. We are a B2B provider.

```html
<!DOCTYPE html>
<html lang="en">
<head>
<meta charset="utf-8">
<title>Meridian Play Systems – Live Casino Software</title>
<link rel="stylesheet" href="https://fonts.googleapis.com/css2?family=Arimo:wght@400;700&family=Carlito:wght@400;700&display=swap">
<style>
  :root {
    --page-bg: #e6e6e6;
    --sheet: #ffffff;
    --ink: #222222;
    --body-text: #333333;
    --muted: #666666;
    --brand-blue: #1a86bd;
    --brand-dark: #0f4f74;
    --accent-orange: #e8772e;
    --panel-edge: #d4d4d4;
    --panel-fill: #f6f6f6;
    --band-black: #000000;
    --dot: #cfcfcf;
  }
  * { margin: 0; padding: 0; box-sizing: border-box; }
  html, body { width: 1200px; height: 935px; overflow: hidden; }
  body {
    background: var(--page-bg);
    font-family: "Arimo", Arial, sans-serif;
    color: var(--ink);
    position: relative;
  }
  .sheet {
    position: absolute; left: 160px; top: 17px; width: 880px; height: 884px;
    background: var(--sheet); border-radius: 4px;
    box-shadow: 0 0 6px rgba(0,0,0,.12);
  }
  .brand {
    position: absolute; left: 197px; top: 38px;
    display: flex; align-items: center; gap: 8px;
    font-family: "Arimo", Arial, sans-serif; font-weight: 700;
    font-size: 17px; color: var(--brand-dark);
  }
  .brand-dot { width: 30px; height: 30px; border-radius: 50%; background: var(--brand-blue); }
  .main-nav {
    position: absolute; top: 49px; left: 443px;
    display: flex; gap: 0; font-size: 14px;
  }
  .main-nav a {
    color: var(--ink); text-decoration: none; padding: 4px 9px; height: 23px; line-height: 16px;
    position: relative; margin-right: 1px;
  }
  .main-nav a.active { background: var(--brand-dark); color: #fff; margin-right: 2px; }
  .main-nav a.active::after {
    content: ""; position: absolute; left: 50%; bottom: -6px; margin-left: -6px;
    border: 6px solid transparent; border-bottom: 0; border-top-color: var(--brand-dark);
  }
  .hero {
    position: absolute; left: 151px; top: 100px; width: 898px; height: 211px;
    background: linear-gradient(#fafafa, #ececec);
    border: 1px solid #dcdcdc;
    box-shadow: 0 2px 5px rgba(0,0,0,.15);
  }
  .hero-photo {
    position: absolute; left: 0; top: 20px; width: 440px; height: 180px;
    background: linear-gradient(90deg, #d7dadd 0%, #c4c8cc 50%, #e6e7e8 100%);
    opacity: .8;
  }
  .hero-title {
    position: absolute; left: 457px; top: 33px;
    font-family: "Carlito", Calibri, sans-serif; font-size: 29px; font-weight: 700;
    color: var(--brand-blue);
  }
  .hero-sub {
    position: absolute; left: 459px; top: 82px; font-size: 13.5px; line-height: 21px; color: var(--ink);
  }
  .hero-dots { position: absolute; left: 800px; top: 186px; display: flex; gap: 5px; }
  .hero-dots span { width: 12px; height: 12px; border-radius: 50%; background: var(--dot); }
  .hero-dots span.current { background: var(--brand-blue); }

  .panel {
    position: absolute; left: 169px; width: 420px;
    background: linear-gradient(#ffffff, var(--panel-fill));
    border: 1px solid var(--panel-edge);
  }
  .dealers { top: 321px; height: 235px; }
  .dealer-frame {
    position: absolute; background: #fff; padding: 5px;
    box-shadow: 0 1px 4px rgba(0,0,0,.35);
  }
  .dealer-frame div { width: 100%; height: 100%; }
  .dealer-left { left: 68px; top: 28px; width: 116px; height: 106px; }
  .dealer-right { left: 215px; top: 32px; width: 127px; height: 104px; }
  .dealer-center { left: 140px; top: 58px; width: 132px; height: 92px; }
  .dealer-left div { background: linear-gradient(135deg, #3a2a24, #a07a66); }
  .dealer-right div { background: linear-gradient(135deg, #5a2018, #9a6a58); }
  .dealer-center div { background: linear-gradient(135deg, #2c1f1a, #c09280); }
  .dealers-title {
    position: absolute; left: 0; right: 0; top: 175px; text-align: center;
    font-family: "Carlito", Calibri, sans-serif; font-size: 19px; color: var(--accent-orange);
  }
  .dealers-sub { position: absolute; left: 0; right: 0; top: 203px; text-align: center; font-size: 11.5px; color: var(--body-text); }

  .news { top: 566px; height: 190px; }
  .news h2 { position: absolute; left: 28px; top: 20px; font-size: 18.5px; font-weight: 700; color: var(--ink); }
  .news-list { position: absolute; left: 28px; top: 59px; width: 370px; list-style: none; }
  .news-list li {
    display: flex; font-size: 11.5px; height: 23.5px; line-height: 23.5px;
    border-bottom: 1px solid #e6e6e6;
  }
  .news-list li:last-child { border-bottom: 0; }
  .news-date { width: 70px; color: var(--muted); }
  .news-title { font-weight: 700; color: var(--ink); }

  .intro {
    position: absolute; left: 632px; top: 352px; width: 372px;
    font-size: 12.8px; line-height: 23.5px; color: var(--ink);
  }
  .call-band {
    position: absolute; left: 160px; top: 773px; width: 881px; height: 34px;
    background: var(--band-black); display: flex; align-items: center; color: #fff;
  }
  .call-label {
    width: 179px; height: 100%; background: var(--brand-dark);
    display: flex; align-items: center; gap: 14px; padding-left: 14px; font-size: 16px;
  }
  .call-number { padding-left: 13px; font-size: 15px; }
  .call-number strong { font-size: 21px; margin-right: 4px; }
  .about {
    position: absolute; left: 197px; top: 828px; width: 792px;
    font-size: 10.6px; line-height: 17px; color: var(--muted);
  }
  .about a { color: var(--muted); }
  .copyright { position: absolute; left: 168px; top: 910px; font-size: 11px; color: var(--muted); }
  .footer-links { position: absolute; right: 188px; top: 910px; font-size: 11.5px; color: var(--muted); }
  .footer-links a { color: var(--brand-blue); text-decoration: none; }
</style>
</head>
<body>
  <div class="sheet"></div>

  <header>
    <div class="brand"><span class="brand-dot"></span>Meridian Play Systems</div>
    <nav class="main-nav">
      <a class="active" href="#">Home</a>
      <a href="#">Live Games</a>
      <a href="#">Our Solutions</a>
      <a href="#">Videos</a>
      <a href="#">News And Events</a>
      <a href="#">About Us</a>
      <a href="#">Contact Us</a>
    </nav>
  </header>

  <section class="hero">
    <div class="hero-photo" role="img" aria-label="Business people running ahead in a line"></div>
    <h1 class="hero-title">Stay Ahead of the Competition</h1>
    <p class="hero-sub">We Deliver Cutting Edge Technology to the Most<br>Advanced Companies in the Industry</p>
    <div class="hero-dots"><span class="current"></span><span></span><span></span><span></span><span></span></div>
  </section>

  <section class="panel dealers">
    <div class="dealer-frame dealer-left"><div role="img" aria-label="Portrait of a live dealer"></div></div>
    <div class="dealer-frame dealer-right"><div role="img" aria-label="Portrait of a live dealer"></div></div>
    <div class="dealer-frame dealer-center"><div role="img" aria-label="Portrait of a live dealer"></div></div>
    <h2 class="dealers-title">GET TO KNOW OUR BEAUTIFUL DEALERS</h2>
    <p class="dealers-sub">They Will Ensure Your Players are Smiling Even when Losing!</p>
  </section>

  <section class="panel news">
    <h2>Latest News and Events</h2>
    <ul class="news-list">
      <li><span class="news-date">2011.03.09</span><span class="news-title">MPS featured in LatAm Gaming Forum 2011 in Panama</span></li>
      <li><span class="news-date">2010.06.12</span><span class="news-title">15 units of kiosk delivered to Mexico</span></li>
      <li><span class="news-date">2010.05.10</span><span class="news-title">"LUCKY ORBIT" set to implement Live Dealer product</span></li>
      <li><span class="news-date">2010.05.06</span><span class="news-title">New High Definition video equipment placed in studio</span></li>
      <li><span class="news-date">2010.04.26</span><span class="news-title">Hours of operation extended</span></li>
    </ul>
  </section>

  <section class="intro">
    <p>Lorem ipsum dolor sit amet, consectetur adipisicing elit, sed do eiusmod tempor incididunt ut labore et dolore magna aliqua. Ut enim ad minim veniam, quis nostrud exercitation ullamco laboris nisi ut aliquip ex ea commodo consequat. Duis aute irure dolor in reprehenderit in voluptate velit esse cillum dolore eu fugiat nulla pariatur. Excepteur sint occaecat cupidatat non proident, sunt in culpa qui officia deserunt mollit anim id est laborum.</p>
    <p>Lorem ipsum dolor sit amet, consectetur adipisicing elit, sed do eiusmod tempor incididunt ut labore et dolore magna aliqua. Ut enim ad minim veniam, quis nostrud exercitation ullamco laboris nisi ut aliquip ex ea commodo consequat. Duis aute irure dolor in reprehenderit in voluptate velit esse cillum dolore eu fugiat nulla pariatur. Excepteur sint occaecat cupidatat non proident, sunt in culpa qui officia deserunt mollit anim id est laborum.</p>
  </section>

  <section class="call-band">
    <div class="call-label">
      <svg width="10" height="20" viewBox="0 0 10 20" aria-hidden="true"><path d="M8 1 C3 2 1 6 1 10 C1 14 3 18 8 19" fill="none" stroke="#fff" stroke-width="2.2" stroke-linecap="round"/></svg>
      CALL TOLL FREE
    </div>
    <div class="call-number"><strong>1-XXXXXX-XXX</strong> and get a FREE Demo of our Software and Solutions</div>
  </section>

  <p class="about">Meridian Play Systems is a leader among <a href="#">online casino software providers</a>. Our team of expert <a href="#">internet casino software developers</a>, managers and marketers are here to ensure that any project you need, is a project Meridian Play Systems can deliver. Our Casino services and consulting solutions can take your business to the next level. Our <a href="#">online casino software licensing</a> can help any start up achieve the quickest and most secure return on investment.</p>

  <footer>
    <p class="copyright">Meridian Play Systems © 2011</p>
    <p class="footer-links"><a href="#">About</a> · <a href="#">Careers</a> · <a href="#">Privacy</a> · <a href="#">Terms</a> · <a href="#">Help</a></p>
  </footer>
</body>
</html>
```